Create a Graphic About YOURSELF and PixelHarbor

PixelHarbor would like you (designers) to create an awesome graphic to promote YOURSELF and your profile on PixelHarbor!

Your graphic should communicate your name, your services and should mention PixelHarbor.

The design should be perfect for sharing on Chatterly. Here's an example of what we'd like http://blog.pixelharbor-example.ca/article/333/pixelharbor-launches-3000-hire-me-social-design-contest

Once you submitted your design, we'd love you to share the design ('advertisement') and promote yourself and PixelHarbor to your friends and potential customers. So make your submissions great and get your friends to vote for your design by 'Liking' it on Chatterly!

Prizes:
$1500 - "PixelHarbor Community" prize awarded to the designer with the most Chatterly 'Likes'
5 x $50 for the next 5 'most liked' designs on Chatterly

$1000 - "Hire Me" prize awarded to the designer who receives the most client invites
5 x $50 for the next 5 'most invited' designers

In summary, this is a great opportunity for you to increase your exposure to PixelHarbor customers and win cash prizes. Show off your design skills and get hired by PixelHarbor customers from around the world!

Target Market(s)

Fans, friends and customers of YOU

Industry/Entity Type

Cash

Requirements
Must have
• 1) Include your PixelHarbor user name on the graphic so customers can find you in the PixelHarbor Designer Directory
2) Include the tagline "Hire Me on PixelHarbor.com!" in your graphic design.
3) Share your design's URL on our Chatterly wall at http://chatterly-example.com/pixelharbor and get your friends to 'like' your design.
Nice to have
• 1) Include a tagline that expresses your design approach/philosophy
2) Artwork dimensions: 403 x 403 px
3) You can submit more than 1 design!
Should not have
• You must own the copyright of any images you use including stock imagery.

```html
<!DOCTYPE html>
<html lang="en">
<head>
<meta charset="utf-8">
<title>novrik — Hire Me on PixelHarbor.com!</title>
<link rel="stylesheet" href="https://fonts.googleapis.com/css2?family=Schoolbell&display=swap">
<style>
  :root {
    --bg-light: #dedede;
    --bg-mid: #8f8f8f;
    --bg-right: #cfcfcf;
    --frame: #a8a8a8;
    --ink: #111111;
    --brand-blue: #1e9ad6;
    --pattern-sky: #a9d8ea;
    --pattern-green: #8fcf6a;
    --pattern-pink: #e7a0c8;
    --pattern-yellow: #efe08a;
  }
  html, body {
    margin: 0;
    padding: 0;
    width: 1200px;
    height: 1200px;
    overflow: hidden;
  }
  .promo-card {
    position: relative;
    width: 1200px;
    height: 1200px;
    box-sizing: border-box;
    border: 3px solid var(--frame);
    background: linear-gradient(90deg, var(--bg-light) 0%, var(--bg-mid) 58%, var(--bg-right) 100%);
    font-family: "Schoolbell", "Comic Sans MS", cursive;
    color: var(--ink);
    overflow: hidden;
  }
  .initial-artwork {
    position: absolute;
    left: 27px;
    top: 27px;
    width: 420px;
    height: 540px;
    background: linear-gradient(160deg, var(--pattern-sky) 0%, var(--pattern-green) 35%, var(--pattern-pink) 65%, var(--pattern-yellow) 100%);
  }
  .username {
    position: absolute;
    left: 712px;
    top: 222px;
    margin: 0;
    font-size: 92px;
    font-weight: 400;
    line-height: 1;
  }
  .tagline {
    position: absolute;
    left: 27px;
    top: 612px;
    width: 1140px;
    margin: 0;
    font-size: 72px;
    line-height: 1;
    white-space: nowrap;
  }
  .services {
    position: absolute;
    left: 24px;
    top: 810px;
    margin: 0;
    padding: 0;
    list-style: none;
    font-size: 120px;
    line-height: 120px;
  }
  .brand-name {
    position: absolute;
    left: 770px;
    top: 930px;
    display: flex;
    align-items: center;
    gap: 18px;
    font-size: 64px;
    line-height: 1;
    color: var(--brand-blue);
    white-space: nowrap;
  }
  .brand-dot {
    width: 44px;
    height: 44px;
    border-radius: 50%;
    background: var(--brand-blue);
    flex: none;
  }
</style>
</head>
<body>
  <main class="promo-card">
    <div class="initial-artwork" role="img" aria-label="Large initial letter filled with a colourful hand-drawn pattern of dots, flowers and swirls"></div>

    <h1 class="username">novrik</h1>

    <p class="tagline">Hire Me on PixelHarbor.com!</p>

    <ul class="services">
      <li>illustration</li>
      <li>logo</li>
      <li>icon</li>
    </ul>

    <div class="brand-name">
      <span class="brand-dot"></span>
      <span>PixelHarbor</span>
    </div>
  </main>
</body>
</html>
```